"Drink Champagne and Dance on the Table" sort of business card needed!

We throw events, weddings, engagement parties, baby showers and the sort of end of year corporate events that people remember long after the glitter has settled - the sort of events that make you stand still and say wow when you walk in and then make you want to "Drink Champagne and Dance on the Tables"

We have a great logo with heaps of potential and need a business card that just screams creative professionals!

We are based in Auckland, NZ and are priced at the Premium end of the market were there are around 10 other main competitors. We need to stand out and make a strong statement about who we are!

Our Business Card will be one of the few items that we print out so are fully prepared to invest in a premium print job.

We really love our logo and think it has heaps of potential! Its ok if you would like to manipulate it (maybe put it on an angle, or use the circle element on its own?).

Black and Gold is very striking, but its very done in our market so we would like to avoid a solid black background please

We have done a bit of an inspiration document to give you an idea of the sort of look and feel we are hoping to achieve.

Target Market(s)

Woman aged 30 - 45 with an income bracket of $70k +

Industry/Entity Type

Event Planning

Contact Information for Business Card

Marnie
hello@fennwhistle.co.nz
www.fennwhistle.co.nz
02739418207

Number of Pages Required

5+ page

Requirements
Must have
• Vibrant colours and design (we love the vibrant pink and gold in the inspiration file)
• We would love to see some colour and creativity (although the black and gold is very striking). Because we are doing such minimal print work I am happy for the cards to be a little more expensive so if you want to use cut outs, rounded corners, gold foil, non standard size etc I am happy for that too. I really want the wow factor.
Nice to have
• We would like the design to be double sided.
Should not have
• The logo colour changed
• Use of Purple or Green or solid black background.
• Wedding Photos!

```html
<!DOCTYPE html>
<html lang="en">
<head>
<meta charset="UTF-8">
<title>Fenn and Whistle – Business Card</title>
<link rel="stylesheet" href="https://fonts.googleapis.com/css2?family=Playfair+Display:wght@400;700&family=Montserrat:wght@400&display=swap">
<style>
  :root {
    --backdrop: #ecebe8;
    --pink: #f0338a;
    --pink-deep: #e62a80;
    --gold: #d2b062;
    --paper: #ffffff;
    --ink: #1c1c1c;
  }
  * { margin: 0; padding: 0; box-sizing: border-box; }
  html, body {
    width: 1200px; height: 720px; overflow: hidden;
    background: var(--backdrop);
  }
  .canvas {
    position: relative; width: 1200px; height: 720px;
  }
  .card {
    position: absolute; top: 215px; width: 500px; height: 290px;
    filter: drop-shadow(0 8px 18px rgba(0,0,0,0.14));
  }
  .card--front { left: 70px; }
  .card--back { left: 630px; }
  .card__shape { position: absolute; inset: 0; width: 500px; height: 290px; }
  .card__content {
    position: absolute; inset: 0;
    display: flex; flex-direction: column; align-items: center; justify-content: center;
  }

  /* Front */
  .brand { display: flex; flex-direction: column; align-items: center; }
  .brand__circle {
    width: 84px; height: 84px; border-radius: 50%;
    border: 3px solid var(--gold); margin-bottom: 18px;
  }
  .brand__name {
    font-family: "Playfair Display", serif; font-weight: 700;
    font-size: 40px; color: var(--gold); letter-spacing: 0.5px; line-height: 1;
  }
  .brand__tagline {
    display: flex; align-items: center; gap: 10px; margin-top: 10px;
    font-family: "Montserrat", sans-serif; font-size: 11px;
    letter-spacing: 4px; color: var(--gold);
  }
  .brand__tagline::before, .brand__tagline::after {
    content: ""; width: 22px; height: 1px; background: var(--gold);
  }

  /* Back */
  .contact__name {
    font-family: "Playfair Display", serif; font-weight: 700;
    font-size: 30px; color: var(--pink); letter-spacing: 1px;
  }
  .contact__divider {
    position: relative; width: 300px; height: 24px; margin: 14px 0 12px;
    display: flex; align-items: center; justify-content: center; gap: 8px;
  }
  .contact__divider::before {
    content: ""; position: absolute; left: 0; right: 0; top: 50%;
    height: 1px; background: var(--pink);
  }
  .contact__icon {
    position: relative; width: 22px; height: 22px; border-radius: 50%;
    background: var(--pink); display: flex; align-items: center; justify-content: center;
  }
  .contact__icon svg { width: 12px; height: 12px; }
  .contact__list { list-style: none; text-align: center; }
  .contact__item {
    font-family: "Playfair Display", serif; font-size: 17px;
    color: var(--ink); line-height: 1.6;
  }
  .contact__accent { color: var(--pink); }
</style>
</head>
<body>
<main class="canvas">

  <section class="card card--front" aria-label="Card front">
    <svg class="card__shape" viewBox="0 0 500 290" aria-hidden="true">
      <path fill="var(--pink)" d="M30,0 H470 Q500,0 500,30 V60 C500,80 482,80 482,100 V190 C482,210 500,210 500,230 V260 Q500,290 470,290 H30 Q0,290 0,260 V230 C0,210 18,210 18,190 V100 C18,80 0,80 0,60 V30 Q0,0 30,0 Z"/>
    </svg>
    <div class="card__content">
      <div class="brand">
        <span class="brand__circle" aria-hidden="true"></span>
        <h1 class="brand__name">Fenn and Whistle</h1>
        <p class="brand__tagline">WEDDINGS &amp; EVENTS</p>
      </div>
    </div>
  </section>

  <section class="card card--back" aria-label="Card back">
    <svg class="card__shape" viewBox="0 0 500 290" aria-hidden="true">
      <path fill="var(--paper)" stroke="var(--pink)" stroke-width="2" d="M30,1 H470 Q499,1 499,30 V60 C499,80 481,80 481,100 V190 C481,210 499,210 499,230 V260 Q499,289 470,289 H30 Q1,289 1,260 V230 C1,210 19,210 19,190 V100 C19,80 1,80 1,60 V30 Q1,1 30,1 Z"/>
    </svg>
    <div class="card__content">
      <h2 class="contact__name">MARNIE ASHDOWN</h2>
      <div class="contact__divider" aria-hidden="true">
        <span class="contact__icon">
          <svg viewBox="0 0 12 12"><path fill="#fff" d="M2.5 1 L4.5 1 L5 3.5 L3.8 4.4 Q4.8 6.7 7.6 8.2 L8.5 7 L11 7.5 L11 9.5 Q11 11 9.5 11 Q1 10 1 2.5 Q1 1 2.5 1 Z"/></svg>
        </span>
        <span class="contact__icon">
          <svg viewBox="0 0 12 12"><rect x="1" y="2.5" width="10" height="7" fill="#fff"/><path d="M1 2.5 L6 6.5 L11 2.5" fill="none" stroke="var(--pink)" stroke-width="1"/></svg>
        </span>
        <span class="contact__icon">
          <svg viewBox="0 0 12 12" fill="none" stroke="#fff" stroke-width="1"><circle cx="6" cy="6" r="4.8"/><ellipse cx="6" cy="6" rx="2" ry="4.8"/><path d="M1.2 6 H10.8 M2 3.5 H10 M2 8.5 H10"/></svg>
        </span>
      </div>
      <ul class="contact__list">
        <li class="contact__item">02739418207</li>
        <li class="contact__item">hello@fennwhistle.co.nz</li>
        <li class="contact__item">www.<span class="contact__accent">fennwhistle</span>.co.nz</li>
      </ul>
    </div>
  </section>

</main>
</body>
</html>
```